Gardener needs an A5 leaflet designed modern and trendy

I am a gardener looking to increase business. I am hoping for a leaflet that is informative and eye catching to do this. I would like the flyer to be in keeping with my business card and website. www.brookvaleturfcare.co.uk

Target Market(s)

Home owners with money to spend on garden

Industry/Entity Type

Gardener

Colors
000000
acd037

Requirements
Must have
• Pictures to show nice lawns/gardens
• explain what we do as a company. ( see business card for bullet points of what we do)
• 10% off all quoted work with this leaflet ( must be shown when quoting)

```html
<!DOCTYPE html>
<html lang="en">
<head>
<meta charset="utf-8">
<title>Brookvale Turf Care – Leaflet</title>
<link href="https://fonts.googleapis.com/css2?family=Questrial&display=swap" rel="stylesheet">
<style>
  :root {
    --leaf: #8fbf2a;
    --leaf-dark: #5f8f1c;
    --lime: #acd037;
    --ink: #111111;
    --paper: #ffffff;
    --charcoal: #1e2320;
  }
  * { margin: 0; padding: 0; box-sizing: border-box; }
  html, body { width: 847px; height: 1200px; overflow: hidden; background: var(--paper); }
  body { font-family: "Questrial", Arial, sans-serif; color: var(--ink); }
  .leaflet { position: relative; width: 847px; height: 1200px; overflow: hidden; background: var(--paper); }

  .hero-photo {
    position: absolute; left: 0; top: 0; width: 847px; height: 400px;
    background: linear-gradient(160deg, #c9793f 0%, #6f8f3c 30%, #3f6b2a 55%, #2f5a22 80%, #4d7a35 100%);
  }
  .brand-panel {
    position: absolute; right: 0; top: 0; width: 290px; height: 180px;
    background: var(--charcoal); border-bottom-left-radius: 40px;
    display: flex; flex-direction: column; align-items: center; justify-content: center; gap: 12px;
  }
  .brand-mark { width: 24px; height: 24px; border-radius: 50%; background: var(--lime); }
  .brand-name { color: var(--lime); font-size: 28px; text-align: center; line-height: 1.15; letter-spacing: 1px; }

  .swoosh { position: absolute; left: 0; top: 290px; width: 847px; height: 120px; }

  .services { position: absolute; left: 22px; top: 392px; width: 590px; }
  .section-title { color: var(--leaf); font-size: 28px; font-weight: 400; line-height: 34px; margin: 0 0 3px; }
  .section { margin-bottom: 10px; }
  .bullet-list { list-style: none; display: grid; grid-template-columns: 300px 278px; column-gap: 12px; }
  .bullet-list li { font-size: 17px; line-height: 21px; padding-left: 14px; position: relative; }
  .bullet-list li::before { content: "•"; position: absolute; left: 0; }

  .photo-column { position: absolute; right: 0; top: 430px; width: 225px; }
  .photo { width: 225px; margin-bottom: 14px; border-radius: 4px 0 0 4px; }
  .photo-stone { height: 130px; background: linear-gradient(135deg, #9aa07a, #5e7a35 60%, #3f5e22); }
  .photo-lawn { height: 150px; background: linear-gradient(180deg, #7fae3a, #4f8a25); }
  .photo-sprinkler { height: 150px; background: linear-gradient(180deg, #b9c9c4, #6f8f5a 60%, #3c6a2a); }
  .photo-planting {
    position: absolute; right: 0; top: 1010px; width: 320px; height: 190px;
    border-top-left-radius: 160px;
    background: linear-gradient(135deg, #d7a23c, #7ea640 45%, #3f6d2a);
  }

  .contact-curve { position: absolute; left: 0; top: 985px; width: 847px; height: 215px; }
  .contact { position: absolute; left: 22px; top: 1020px; }
  .contact-phone { color: var(--leaf); font-size: 48px; letter-spacing: 1px; line-height: 1; margin-bottom: 8px; }
  .contact-line { font-size: 22px; line-height: 27px; }
  .contact-offer { font-size: 17px; line-height: 24px; color: var(--leaf-dark); margin-top: 4px; }
</style>
</head>
<body>
<main class="leaflet">
  <div class="hero-photo" role="img" aria-label="Photo of a lush landscaped garden with flowering borders and a fence"></div>

  <div class="brand-panel">
    <span class="brand-mark"></span>
    <span class="brand-name">BROOKVALE<br>TURF CARE</span>
  </div>

  <svg class="swoosh" viewBox="0 0 847 120" preserveAspectRatio="none" aria-hidden="true">
    <path d="M0 50 C250 5 550 5 847 30 L847 120 L0 120 Z" fill="var(--leaf)"/>
    <path d="M0 78 C260 35 560 35 847 60 L847 120 L0 120 Z" fill="var(--lime)"/>
    <path d="M0 102 C280 68 580 70 847 90 L847 120 L0 120 Z" fill="var(--paper)"/>
  </svg>

  <section class="services">
    <div class="section">
      <h2 class="section-title">Our Commitment</h2>
      <ul class="bullet-list">
        <li>All waste removed</li><li>Reliable, Prompt and Flexible to suit the customer</li>
        <li>Fully Insured</li><li>Free no obligation quotes</li>
        <li>Fully qualified greenkeepers</li>
      </ul>
    </div>
    <div class="section">
      <h2 class="section-title">Garden Services</h2>
      <ul class="bullet-list">
        <li>Garden Clearances</li><li>Artificial Grass Installation</li>
        <li>Regular maintenance programmes</li><li>Irrigation system installation</li>
        <li>Hedge cutting</li><li>Landscaping Design</li>
        <li>Flagging, Paving, Decking and Fencing</li>
      </ul>
    </div>
    <div class="section">
      <h2 class="section-title">Tree Services</h2>
      <ul class="bullet-list">
        <li>Tree pruning</li><li>Tree felling</li>
        <li>Tree shaping</li><li>Tree stump removal</li>
      </ul>
    </div>
    <div class="section">
      <h2 class="section-title">Lawn Services</h2>
      <ul class="bullet-list">
        <li>Turfing</li><li>Scarification</li>
        <li>Weed, Pest and Moss control</li><li>Top Dressing</li>
        <li>Fertiliser applications</li><li>Flexible renovation programmes</li>
        <li>Aeration</li>
      </ul>
    </div>
  </section>

  <aside class="photo-column">
    <div class="photo photo-stone" role="img" aria-label="Photo of a garden feature stone among planting"></div>
    <div class="photo photo-lawn" role="img" aria-label="Photo of a freshly striped lawn"></div>
    <div class="photo photo-sprinkler" role="img" aria-label="Photo of a lawn irrigation sprinkler in use"></div>
  </aside>

  <svg class="contact-curve" viewBox="0 0 847 215" preserveAspectRatio="none" aria-hidden="true">
    <path d="M0 0 C150 25 350 18 560 0 C400 35 180 38 0 26 Z" fill="var(--lime)"/>
    <path d="M0 185 C200 170 400 180 560 203 L560 215 L0 215 Z" fill="var(--leaf)"/>
  </svg>

  <div class="photo-planting" role="img" aria-label="Photo of colourful flower planting and garden tools"></div>

  <div class="contact">
    <p class="contact-phone">07700 900 214</p>
    <p class="contact-line">info@brookvaleturfcare.co.uk</p>
    <p class="contact-line">www.brookvaleturfcare.co.uk</p>
    <p class="contact-offer">10% off all quoted work with this leaflet</p>
  </div>
</main>
</body>
</html>
```